RivoPlex PowerPoint Template with existing Logo and Letterhead template

Develop a PowerPoint template based on existing logo and letterhead designs for a Marketing Consultancy.
Presentations that will be made with title slide, content slides (which includes mostly bullet point text and some tables) and also last page company introduction and copyright.
Corporate colors should be keep as per the logo

I like something like from Artisan Hive
- Serious, Modern PowerPoint Design for Company in Canada | Design 418674
- Professional, Modern PowerPoint Design for Company in United States | Design 7795293
- Professional, Modern PowerPoint Design for Company in United States | Design 7826742
- Serious, Modern PowerPoint Design for Company in Canada | Design 418635
- Elegant, Serious PowerPoint Design for Company in Puerto Rico | Design 16951178
- Bold, Modern PowerPoint Design for Company in United States | Design 11745238

To all designers, • We need sleek and modern looking PowerPoint presentation template. • The template will primarily be used for our corporate slide and solutions presentation for our customers. • Not too much of white and it should be sleek, modern and impressive for marketing consultancy firms like us. • Please ensure the content pages are water marketed with the 4 boxes. • I like something like from Artisan Hive and you can get some idea on what I like.: o Serious, Modern PowerPoint Design for Company in Canada | Design 418674 o Professional, Modern PowerPoint Design for Company in United States | Design 7795293 o Professional, Modern PowerPoint Design for Company in United States | Design 7826742 o Serious, Modern PowerPoint Design for Company in Canada | Design 418635 o Elegant, Serious PowerPoint Design for Company in Puerto Rico | Design 16951178 o Bold, Modern PowerPoint Design for Company in United States | Design 11745238 Thanks!

Target Market(s)

Marketing Managers, B2B Marketing Team, CRM Data Owners

Industry/Entity Type

Marketing

Requirements
Must have
• Not too much of white and it should be sleek, modern and impressive for marketing consultancy firms like us. Please ensure the content pages are water marketed with the 4 boxes. The template will primarily be used for our corporate slides and solutions presentation for our customers.
Should not have
• no background in the slide content area

```html
<!DOCTYPE html>
<html lang="en">
<head>
<meta charset="utf-8">
<title>RivoPlex Presentation Template</title>
<link href="https://fonts.googleapis.com/css2?family=Open+Sans:wght@300;400;600;700&display=swap" rel="stylesheet">
<style>
:root{
  --red:#e8242b;
  --slate:#4d566a;
  --slate-2:#5d6679;
  --slate-3:#6e7688;
  --dark:#3b3b40;
  --ink:#555b66;
  --muted:#a7abb3;
  --sheet:#e9eaec;
  --white:#ffffff;
}
*{box-sizing:border-box;margin:0;padding:0}
html,body{width:1031px;height:1200px;overflow:hidden;background:var(--sheet);font-family:'Open Sans',Arial,sans-serif;color:var(--ink)}
.sheet{display:grid;grid-template-columns:repeat(3,338px);grid-auto-rows:190px;gap:8px 6px;padding:6px 3px}
.slide{position:relative;overflow:hidden;background:var(--white);box-shadow:0 1px 3px rgba(0,0,0,.18)}
.a{position:absolute}
.photo{position:absolute;background:linear-gradient(160deg,#c9d0da,#77818f 55%,#3f4652)}
.photo.sky{background:linear-gradient(180deg,#9fb3cf,#dfe6ef 45%,#7a8697)}
.photo.glass{background:linear-gradient(135deg,#7fa4cf,#c7d6e8 50%,#5a6e88)}
.photo.steel{background:linear-gradient(45deg,#2f343c,#8d96a3 50%,#d5d9df)}
.brand{position:absolute;display:flex;align-items:center;gap:3px;font-weight:700;color:var(--red);letter-spacing:.5px}
.brand i{display:block;background:var(--red)}
.brand.sm{top:12px;right:10px;font-size:9px}
.brand.sm i{width:4px;height:4px}
.title{position:absolute;left:16px;top:12px;font-size:11.5px;font-weight:300;color:var(--ink)}
.title::after{content:"";position:absolute;left:0;bottom:-6px;width:16px;height:1.5px;background:var(--red)}
.foot{position:absolute;left:0;right:0;bottom:0;height:8px;background:var(--slate);color:#d7dae0;font-size:3px;line-height:8px;padding-left:16px}
.pg{position:absolute;right:22px;bottom:0;width:8px;height:8px;background:var(--red);color:#fff;font-size:3px;text-align:center;line-height:8px}
.mark{position:absolute;right:26px;bottom:12px;width:7px;height:7px;background:var(--slate)}
.tiny{font-size:3.3px;line-height:1.45;color:var(--muted)}
.tiny.w{color:rgba(255,255,255,.85)}
.hd{font-size:5.5px;color:var(--ink)}
.hd.r{color:var(--red)}
.hd.w{color:#fff}
.dot{display:inline-block;width:9px;height:9px;border-radius:2px;background:var(--red)}
.ic{width:9px;height:9px;border-radius:50%;background:var(--dark)}
.ic.r{background:var(--red)}
</style>
</head>
<body>
<main class="sheet">

<!-- 1 cover -->
<section class="slide">
  <div class="photo" style="left:0;top:0;width:338px;height:142px" role="img" aria-label="Upward view of a glass skyscraper against a cloudy sky"></div>
  <div class="a" style="left:29px;top:76px;color:#fff;font-size:17px;font-weight:300">Your Title Goes Here</div>
  <div class="a" style="left:29px;top:100px;color:#fff;font-size:5px;font-weight:700">Your Subtitle Goes Here</div>
  <div class="a" style="left:24px;top:175px;font-size:5px;color:#888">www.yourwebsite.com</div>
  <div class="brand" style="right:46px;top:166px;font-size:14px"><i style="width:5px;height:5px"></i>RivoPlex</div>
</section>

<!-- 2 cover light -->
<section class="slide" style="background:#f3f3f4">
  <div class="a" style="left:27px;top:78px;color:var(--red);font-size:17px;font-weight:700">Your Title Here</div>
  <div class="a" style="left:27px;top:102px;color:var(--red);font-size:5px">Your Subtitle Goes Here</div>
  <div class="a" style="left:214px;top:20px;width:28px;height:28px;background:var(--red)"></div>
  <div class="a" style="left:192px;top:72px;width:44px;height:44px;background:var(--slate)"></div>
  <div class="a" style="left:259px;top:56px;width:34px;height:34px;background:var(--slate)"></div>
  <div class="a" style="left:249px;top:114px;width:58px;height:58px;background:var(--red)"></div>
</section>

<!-- 3 cover red -->
<section class="slide" style="background:var(--red)">
  <div class="a" style="left:19px;top:78px;color:#fff;font-size:17px;font-weight:700">Your <span style="color:#f3a2a5">Title Here</span></div>
  <div class="a" style="left:19px;top:104px;color:#fff;font-size:5px;font-weight:600">Your Subtitle Goes Here</div>
  <div class="photo steel" style="left:214px;top:18px;width:27px;height:27px" role="img" aria-label="Glass building facade detail"></div>
  <div class="photo steel" style="left:194px;top:72px;width:43px;height:43px" role="img" aria-label="Glass building facade detail"></div>
  <div class="a" style="left:260px;top:56px;width:34px;height:34px;background:var(--dark)"></div>
  <div class="a" style="left:250px;top:114px;width:58px;height:58px;background:var(--dark)"></div>
</section>

<!-- 4 cover slate -->
<section class="slide" style="background:linear-gradient(180deg,#4d566a,#5a5a68 60%,#8a3c44)">
  <div class="a" style="inset:0;opacity:.35;background:linear-gradient(160deg,#9aa3b2,#3a4152)" role="img" aria-label="Tinted view of a city tower"></div>
  <div class="brand" style="left:0;right:0;top:66px;justify-content:center;font-size:16px"><i style="width:6px;height:6px"></i>RivoPlex</div>
  <div class="a" style="left:0;right:0;top:100px;text-align:center;color:#fff;font-size:17px;font-weight:300">Your Title Goes Here</div>
  <div class="a" style="left:0;right:0;top:125px;text-align:center;color:#fff;font-size:5px;font-weight:700">Your Subtitle Goes Here</div>
</section>

<!-- 5 agenda -->
<section class="slide">
  <div class="title">Our Agenda</div>
  <div class="brand sm"><i></i>RivoPlex</div>
  <div class="a" style="left:46px;top:53px;display:grid;grid-template-columns:136px 120px;row-gap:16px">
    <div style="display:flex;gap:6px"><span class="dot"></span><div><div class="hd">Agenda One</div><div class="tiny">Lorem ipsum dolor sit amet, consectetur<br>adipiscing elit, sed do eiusmod tempor</div></div></div>
    <div style="display:flex;gap:6px"><span class="dot"></span><div><div class="hd">Agenda Four</div><div class="tiny">Lorem ipsum dolor sit amet, consectetur<br>adipiscing elit, sed do eiusmod tempor</div></div></div>
    <div style="display:flex;gap:6px"><span class="dot" style="background:var(--slate)"></span><div><div class="hd">Agenda Two</div><div class="tiny">Lorem ipsum dolor sit amet, consectetur<br>adipiscing elit, sed do eiusmod tempor</div></div></div>
    <div style="display:flex;gap:6px"><span class="dot" style="background:var(--slate)"></span><div><div class="hd">Agenda Five</div><div class="tiny">Lorem ipsum dolor sit amet, consectetur<br>adipiscing elit, sed do eiusmod tempor</div></div></div>
    <div style="display:flex;gap:6px"><span class="dot" style="background:var(--dark)"></span><div><div class="hd">Agenda Three</div><div class="tiny">Lorem ipsum dolor sit amet, consectetur<br>adipiscing elit, sed do eiusmod tempor</div></div></div>
    <div style="display:flex;gap:6px"><span class="dot" style="background:var(--dark)"></span><div><div class="hd">Agenda Six</div><div class="tiny">Lorem ipsum dolor sit amet, consectetur<br>adipiscing elit, sed do eiusmod tempor</div></div></div>
  </div>
  <div class="mark"></div>
  <div class="foot">© Copyright 2017 RivoPlex. All rights reserved.</div><div class="pg">1</div>
</section>

<!-- 6 market overview -->
<section class="slide">
  <div class="title">Market Overview</div>
  <div class="brand sm"><i></i>RivoPlex</div>
  <div class="a" style="left:14px;top:40px;width:70px;height:127px;background:var(--dark);padding:26px 8px">
    <div class="hd w" style="font-size:4.5px">Heading Text</div>
    <div class="tiny w">dolore aliqua lorem ipsum dolor sit amet consectetur adipiscing elit sed do tempor</div>
    <div class="hd w" style="font-size:4.5px;margin-top:22px">Heading Text</div>
    <div class="tiny w">dolore aliqua lorem ipsum dolor sit amet consectetur adipiscing elit sed do tempor</div>
  </div>
  <div class="photo glass" style="left:84px;top:40px;width:86px;height:63px" role="img" aria-label="Skyscraper rising into a blue sky"></div>
  <div class="a" style="left:170px;top:40px;width:84px;height:63px;background:var(--slate)">
    <svg class="a" style="left:17px;top:6px" width="50" height="50" viewBox="0 0 50 50"><circle cx="25" cy="25" r="21" fill="none" stroke="#8790a2" stroke-width="3"/><circle cx="25" cy="25" r="21" fill="none" stroke="var(--red)" stroke-width="3" stroke-dasharray="79 132" transform="rotate(-90 25 25)"/><text x="25" y="29" text-anchor="middle" fill="#fff" font-size="11" font-family="Open Sans,sans-serif" font-weight="300">60%</text></svg>
  </div>
  <div class="a" style="left:254px;top:40px;width:84px;height:63px;background:var(--red);padding:4px 8px">
    <div class="hd w" style="font-size:4px">Heading Text</div>
    <div class="tiny w">dolore aliqua lorem ipsum dolor sit amet consectetur adipiscing</div>
    <div class="hd w" style="font-size:4px;margin-top:3px">Heading Text</div>
    <div class="tiny w">dolore aliqua lorem ipsum dolor sit amet consectetur adipiscing</div>
  </div>
  <div class="a" style="left:91px;top:112px;width:236px">
    <div class="hd r" style="font-size:5px">Heading Text</div>
    <div class="tiny">Dolore aliqua lorem ipsum dolor sit amet, consectetur adipiscing elit, sed do eiusmod tempor incididunt ut labore et dolore magna aliqua. Lorem ipsum dolor sit amet, consectetur adipiscing elit, sed do eiusmod tempor incididunt ut labore et dolore aliqua. Ut enim ad minim veniam quis nostrud exercitation ullamco laboris.</div>
  </div>
  <div class="mark"></div>
  <div class="foot">© Copyright 2017 RivoPlex. All rights reserved.</div><div class="pg">2</div>
</section>

<!-- 7 bullets -->
<section class="slide">
  <div class="title">Bullets Point 1 Level</div>
  <div class="brand sm"><i></i>RivoPlex</div>
  <div class="a" style="left:26px;top:52px;display:grid;grid-template-columns:106px 106px 90px;row-gap:28px">
    <div><div class="hd r" style="font-weight:700;font-size:5px">● Your Text Here</div><div class="tiny" style="padding-left:8px">Lorem ipsum dolor sit<br>consectetur adipiscing elit,<br>sed do eiusmod tempo</div></div>
    <div><div class="hd" style="font-weight:700;font-size:5px">● Your Text Here</div><div class="tiny" style="padding-left:8px">Lorem ipsum dolor sit<br>consectetur adipiscing elit,<br>sed do eiusmod tempo</div></div>
    <div><div class="hd" style="font-weight:700;font-size:5px">● Your Text Here</div><div class="tiny" style="padding-left:8px">Lorem ipsum dolor sit<br>consectetur adipiscing elit,<br>sed do eiusmod tempo</div></div>
    <div><div class="hd r" style="font-weight:700;font-size:5px">● Your Text Here</div><div class="tiny" style="padding-left:8px">Lorem ipsum dolor sit<br>consectetur adipiscing elit,<br>sed do eiusmod tempo</div></div>
    <div><div class="hd" style="font-weight:700;font-size:5px">● Your Text Here</div><div class="tiny" style="padding-left:8px">Lorem ipsum dolor sit<br>consectetur adipiscing elit,<br>sed do eiusmod tempo</div></div>
    <div><div class="hd" style="font-weight:700;font-size:5px">● Your Text Here</div><div class="tiny" style="padding-left:8px">Lorem ipsum dolor sit<br>consectetur adipiscing elit,<br>sed do eiusmod tempo</div></div>
  </div>
  <div class="mark"></div>
  <div class="foot">© Copyright 2017 RivoPlex. All rights reserved.</div><div class="pg">3</div>
</section>

<!-- 8 mosaic -->
<section class="slide">
  <div class="a" style="left:0;top:0;width:169px;height:57px;background:var(--red);padding:5px 19px"><div class="tiny w" style="font-size:4.3px;text-align:justify">Lorem ipsum dolor sit amet consectetur adipiscing elit, sed do eiusmod tempor incididunt ut labore et dolore magna aliqua. Ut enim ad minim veniam, quis nostrud exercitation ullamco laboris nisi ut aliquip ex ea commodo consequat.</div></div>
  <div class="photo sky" style="left:169px;top:0;width:169px;height:57px" role="img" aria-label="Office towers seen from below"></div>
  <div class="photo glass" style="left:0;top:57px;width:169px;height:66px" role="img" aria-label="Blue glass facade"></div>
  <div class="a" style="left:169px;top:57px;width:169px;height:66px;background:var(--slate);padding:14px 19px"><div class="tiny w" style="font-size:4.3px;text-align:justify">Lorem ipsum dolor sit amet consectetur adipiscing elit, sed do eiusmod tempor incididunt ut labore et dolore magna aliqua. Ut enim ad minim veniam, quis nostrud exercitation ullamco laboris nisi ut aliquip ex ea commodo consequat.</div></div>
  <div class="a" style="left:0;top:123px;width:169px;height:67px;background:var(--dark);padding:6px 19px"><div class="tiny w" style="font-size:4.3px;text-align:justify">Lorem ipsum dolor sit amet consectetur adipiscing elit, sed do eiusmod tempor incididunt ut labore et dolore magna aliqua. Ut enim ad minim veniam, quis nostrud exercitation ullamco laboris nisi ut aliquip ex ea commodo consequat.</div></div>
  <div class="photo steel" style="left:169px;top:123px;width:169px;height:67px" role="img" aria-label="Angled steel and glass architecture"></div>
</section>

<!-- 9 four columns -->
<section class="slide">
  <div class="title">Your Title Here</div>
  <div class="brand sm"><i></i>RivoPlex</div>
  <div class="a" style="left:0;top:59px;width:338px;height:99px;display:grid;grid-template-columns:repeat(4,1fr)">
    <div style="background:var(--red);padding:14px 6px;text-align:center"><div class="ic" style="margin:0 auto 8px;width:14px;height:14px;border:1px solid #fff;background:none"></div><div class="hd w">Heading Here</div><div class="tiny w" style="text-align:justify">Lorem ipsum dolor sit amet, consectetur adipiscing elit, sed do eiusmod tempor incididunt ut labore et dolore magna aliqua. Ut enim minim veniam quis nostrud ullamco commodo consequat.</div></div>
    <div style="background:var(--slate);padding:14px 6px;text-align:center"><div class="ic" style="margin:0 auto 8px;width:14px;height:14px;border:1px solid #fff;background:none"></div><div class="hd w">Heading Here</div><div class="tiny w" style="text-align:justify">Lorem ipsum dolor sit amet, consectetur adipiscing elit, sed do eiusmod tempor incididunt ut labore et dolore magna aliqua. Ut enim minim veniam quis nostrud ullamco commodo consequat.</div></div>
    <div style="background:var(--dark);padding:14px 6px;text-align:center"><div class="ic" style="margin:0 auto 8px;width:14px;height:14px;border:1px solid #fff;background:none"></div><div class="hd w">Heading Here</div><div class="tiny w" style="text-align:justify">Lorem ipsum dolor sit amet, consectetur adipiscing elit, sed do eiusmod tempor incididunt ut labore et dolore magna aliqua. Ut enim minim veniam quis nostrud ullamco commodo consequat.</div></div>
    <div style="background:var(--slate-3);padding:14px 6px;text-align:center"><div class="ic" style="margin:0 auto 8px;width:14px;height:14px;border:1px solid #fff;background:none"></div><div class="hd w">Heading Here</div><div class="tiny w" style="text-align:justify">Lorem ipsum dolor sit amet, consectetur adipiscing elit, sed do eiusmod tempor incididunt ut labore et dolore magna aliqua. Ut enim minim veniam quis nostrud ullamco commodo consequat.</div></div>
  </div>
  <div class="mark"></div>
  <div class="foot">© Copyright 2017 RivoPlex. All rights reserved.</div><div class="pg">4</div>
</section>

<!-- 10 differences -->
<section class="slide">
  <div class="title">Our Differences</div>
  <div class="brand sm"><i></i>RivoPlex</div>
  <div class="a" style="left:18px;top:52px;width:302px;height:99px;background:var(--slate);padding:13px 14px;display:flex;flex-direction:column;gap:9px">
    <div style="display:flex;gap:8px;align-items:center"><span class="ic r"></span><span class="tiny w" style="width:130px">Lorem ipsum dolor sit amet, consectetur adipiscing elit, sed do eiusmod tempor incididunt ut labore.</span></div>
    <div style="display:flex;gap:8px;align-items:center"><span class="ic r"></span><span class="tiny w" style="width:130px">Duis aute irure dolor in reprehenderit in voluptate velit esse cillum dolore.</span></div>
    <div style="display:flex;gap:8px;align-items:center"><span class="ic r"></span><span class="tiny w" style="width:130px">Lorem ipsum dolor sit amet, consectetur adipiscing elit, sed do eiusmod tempor incididunt ut labore.</span></div>
    <div style="display:flex;gap:8px;align-items:center"><span class="ic r"></span><span class="tiny w" style="width:130px">Duis aute irure dolor in reprehenderit in voluptate velit esse cillum dolore.</span></div>
  </div>
  <div class="photo steel" style="left:198px;top:62px;width:112px;height:80px" role="img" aria-label="Skyscrapers converging toward the sky"></div>
  <div class="mark"></div>
  <div class="foot">© Copyright 2017 RivoPlex. All rights reserved.</div><div class="pg">5</div>
</section>

<!-- 11 text & bullet -->
<section class="slide">
  <div class="title">Text &amp; Bullet Area</div>
  <div class="brand sm"><i></i>RivoPlex</div>
  <div class="a" style="left:20px;top:52px;width:86px">
    <div class="hd r" style="font-size:5px;margin-bottom:6px">Heading Goes Here</div>
    <div class="tiny">Lorem ipsum dolor sit amet, consectetur adipiscing elit, sed do eiusmod tempor incididunt ut labore et dolore magna aliqua.</div>
    <div class="tiny" style="margin-top:5px">Duis aute irure dolor in reprehenderit in voluptate velit esse cillum dolore eu fugiat nulla pariatur.</div>
    <div class="tiny" style="margin-top:5px">Ut enim minim veniam, quis nostrud exercitation ullamco laboris nisi ut aliquip ex ea commodo consequat.</div>
  </div>
  <div class="a" style="left:124px;top:53px;display:grid;grid-template-columns:107px 90px;row-gap:11px">
    <div style="display:flex;gap:5px"><span class="ic r"></span><div><div class="hd r">Your Text Here</div><div class="tiny">Lorem ipsum dolor sit amet elit</div></div></div>
    <div style="display:flex;gap:5px"><span class="ic"></span><div><div class="hd">Your Text Here</div><div class="tiny">Lorem ipsum dolor sit amet elit</div></div></div>
    <div style="display:flex;gap:5px"><span class="ic" style="background:var(--slate)"></span><div><div class="hd">Your Text Here</div><div class="tiny">Lorem ipsum dolor sit amet elit</div></div></div>
    <div style="display:flex;gap:5px"><span class="ic"></span><div><div class="hd">Your Text Here</div><div class="tiny">Lorem ipsum dolor sit amet elit</div></div></div>
    <div style="display:flex;gap:5px"><span class="ic"></span><div><div class="hd">Your Text Here</div><div class="tiny">Lorem ipsum dolor sit amet elit</div></div></div>
    <div style="display:flex;gap:5px"><span class="ic" style="background:var(--slate)"></span><div><div class="hd">Your Text Here</div><div class="tiny">Lorem ipsum dolor sit amet elit</div></div></div>
    <div style="display:flex;gap:5px"><span class="ic" style="background:var(--muted)"></span><div><div class="hd">Your Text Here</div><div class="tiny">Lorem ipsum dolor sit amet elit</div></div></div>
    <div style="display:flex;gap:5px"><span class="ic r"></span><div><div class="hd r">Your Text Here</div><div class="tiny">Lorem ipsum dolor sit amet elit</div></div></div>
  </div>
  <div class="mark"></div>
  <div class="foot">© Copyright 2017 RivoPlex. All rights reserved.</div><div class="pg">6</div>
</section>

<!-- 12 clients -->
<section class="slide">
  <div class="a" style="left:17px;top:16px;width:304px;height:160px;display:grid;grid-template-columns:repeat(4,1fr);grid-template-rows:repeat(3,1fr);place-items:center">
    <div style="width:44px;height:18px;background:#d7d9dd"></div>
    <div style="width:46px;height:22px;background:#d7d9dd;border-radius:3px"></div>
    <div style="width:46px;height:22px;background:#d7d9dd"></div>
    <div style="width:44px;height:16px;background:#d7d9dd;border-radius:8px"></div>
    <div style="width:40px;height:24px;background:#d7d9dd;border-radius:50%"></div>
    <div></div><div></div>
    <div style="width:44px;height:14px;background:#e2e4e7;border-radius:7px"></div>
    <div style="width:40px;height:24px;background:#d7d9dd"></div>
    <div style="width:36px;height:36px;background:#d7d9dd;border-radius:50%"></div>
    <div style="width:46px;height:24px;background:#d7d9dd"></div>
    <div style="width:44px;height:24px;background:#d7d9dd;border-radius:3px"></div>
  </div>
  <div class="a" style="left:85px;top:66px;width:168px;height:60px;background:var(--red);color:#fff;font-size:15px;font-weight:300;text-align:center;line-height:19px;padding-top:10px">Our Awesome<br>Client</div>
</section>

<!-- 13 five columns -->
<section class="slide">
  <div class="a" style="inset:0;display:grid;grid-template-columns:repeat(5,1fr)">
    <div style="background:var(--slate);padding:48px 7px 0"><div class="ic" style="margin:0 auto 30px;width:20px;height:20px;border:1.2px solid #fff;background:none"></div><div class="hd w" style="font-size:7px">Heading Here</div><div class="tiny w" style="text-align:justify">Lorem ipsum dolor sit amet, consectetur adipiscing elit, sed do eiusmod tempor incididunt ut labore et dolore magna aliqua. Ut enim minim veniam quis nostrud exercitation ullamco laboris.</div></div>
    <div style="background:var(--slate-2);padding:48px 7px 0"><div class="ic" style="margin:0 auto 30px;width:20px;height:20px;border:1.2px solid #fff;background:none"></div><div class="hd w" style="font-size:7px">Heading Here</div><div class="tiny w" style="text-align:justify">Lorem ipsum dolor sit amet, consectetur adipiscing elit, sed do eiusmod tempor incididunt ut labore et dolore magna aliqua. Ut enim minim veniam quis nostrud exercitation ullamco laboris.</div></div>
    <div style="background:var(--slate-3);padding:48px 7px 0"><div class="ic" style="margin:0 auto 30px;width:20px;height:20px;border:1.2px solid #fff;background:none"></div><div class="hd w" style="font-size:7px">Heading Here</div><div class="tiny w" style="text-align:justify">Lorem ipsum dolor sit amet, consectetur adipiscing elit, sed do eiusmod tempor incididunt ut labore et dolore magna aliqua. Ut enim minim veniam quis nostrud exercitation ullamco laboris.</div></div>
    <div style="background:#7e8596;padding:48px 7px 0"><div class="ic" style="margin:0 auto 30px;width:20px;height:20px;border:1.2px solid #fff;background:none"></div><div class="hd w" style="font-size:7px">Heading Here</div><div class="tiny w" style="text-align:justify">Lorem ipsum dolor sit amet, consectetur adipiscing elit, sed do eiusmod tempor incididunt ut labore et dolore magna aliqua. Ut enim minim veniam quis nostrud exercitation ullamco laboris.</div></div>
    <div style="background:var(--red);padding:48px 7px 0"><div class="ic" style="margin:0 auto 30px;width:20px;height:20px;border:1.2px solid #fff;background:none"></div><div class="hd w" style="font-size:7px">Heading Here</div><div class="tiny w" style="text-align:justify">Lorem ipsum dolor sit amet, consectetur adipiscing elit, sed do eiusmod tempor incididunt ut labore et dolore magna aliqua. Ut enim minim veniam quis nostrud exercitation ullamco laboris.</div></div>
  </div>
</section>

<!-- 14 mockup -->
<section class="slide">
  <div class="title">Our Mockup Area</div>
  <div class="brand sm"><i></i>RivoPlex</div>
  <div class="a" style="left:0;right:0;top:59px;bottom:0;background:var(--slate)"></div>
  <svg class="a" style="left:0;top:0" width="338" height="190" viewBox="0 0 338 190">
    <rect x="80" y="38" width="178" height="118" rx="5" fill="#111"/>
    <rect x="86" y="44" width="166" height="104" fill="#fff"/>
    <path d="M62 158 H276 L270 164 H68 Z" fill="#c9ccd2"/>
    <g stroke="#2f3440" stroke-width=".8"><line x1="50" y1="84" x2="165" y2="84"/><line x1="50" y1="111" x2="120" y2="111"/><line x1="50" y1="148" x2="160" y2="148"/><line x1="230" y1="84" x2="288" y2="84"/><line x1="190" y1="111" x2="288" y2="111"/><line x1="175" y1="148" x2="288" y2="148"/></g>
    <g fill="#2f3440"><circle cx="165" cy="84" r="1.4"/><circle cx="120" cy="111" r="1.4"/><circle cx="160" cy="148" r="1.4"/><circle cx="230" cy="84" r="1.4"/><circle cx="190" cy="111" r="1.4"/><circle cx="175" cy="148" r="1.4"/></g>
    <rect x="16" y="79" width="34" height="10" fill="#3b4254"/><rect x="16" y="106" width="34" height="10" fill="#3b4254"/><rect x="16" y="143" width="34" height="10" fill="var(--red)"/>
    <rect x="288" y="79" width="34" height="10" fill="var(--red)"/><rect x="288" y="106" width="34" height="10" fill="#3b4254"/><rect x="288" y="143" width="34" height="10" fill="#3b4254"/>
    <g fill="#fff" font-size="3.2" font-family="Open Sans,sans-serif"><text x="23" y="85">Your Text</text><text x="23" y="112">Your Text</text><text x="23" y="149">Your Text</text><text x="295" y="85">Your Text</text><text x="295" y="112">Your Text</text><text x="295" y="149">Your Text</text></g>
  </svg>
  <div class="brand" style="left:86px;width:166px;top:90px;justify-content:center;font-size:14px"><i style="width:5px;height:5px"></i>RivoPlex</div>
</section>

<!-- 15 right picture -->
<section class="slide">
  <div class="a" style="left:0;top:0;width:170px;height:190px;background:var(--slate)"></div>
  <div class="a" style="left:45px;top:32px;width:80px;height:80px;border:2px solid #fff;border-radius:50%;color:#fff;font-size:10px;font-weight:300;text-align:center;line-height:13px;padding-top:20px"><span style="color:var(--red)">RIGHT</span><br>PICTURE<br>SLIDE</div>
  <div class="a tiny w" style="left:26px;top:131px;width:118px;text-align:center">Mauris quam dolor, cursus at porta et, luctus eget purus. Nunc tempor luctus interdum. Duis libero leo dignissim. Mauris quam dolor, cursus at porta et, luctus eget purus. Nunc tempor luctus interdum.</div>
  <svg class="a" style="left:190px;top:40px" width="130" height="76" viewBox="0 0 130 76">
    <g fill="var(--red)"><rect x="2" y="14" width="4" height="60"/><rect x="30" y="30" width="4" height="44"/><rect x="58" y="24" width="4" height="50"/><rect x="86" y="16" width="4" height="58"/><rect x="114" y="6" width="4" height="68"/></g>
    <g fill="var(--slate)"><rect x="8" y="44" width="4" height="30"/><rect x="36" y="12" width="4" height="62"/><rect x="64" y="40" width="4" height="34"/><rect x="92" y="36" width="4" height="38"/><rect x="120" y="0" width="4" height="74"/></g>
    <g fill="#c7cad0"><rect x="14" y="56" width="4" height="18"/><rect x="42" y="50" width="4" height="24"/><rect x="70" y="58" width="4" height="16"/><rect x="98" y="52" width="4" height="22"/></g>
  </svg>
  <div class="a" style="left:282px;top:120px;font-size:3px;color:#999">■ Sales ■ Market ■ Cost</div>
  <div class="a" style="left:183px;top:132px;font-size:17px;color:var(--dark)"><span style="color:var(--red);font-size:10px">▲</span> 85%</div>
  <div class="a" style="left:198px;top:155px;font-size:4px;font-weight:700;color:var(--dark)">Profit</div>
  <div class="a tiny" style="left:198px;top:161px;width:54px">Mauris quam dolor, cursus at porta et, luctus eget purus. Nunc tempor.</div>
</section>

<!-- 16 mockup red -->
<section class="slide">
  <div class="a" style="left:0;top:0;width:145px;height:95px;background:linear-gradient(180deg,#e8242b,#ee5a5f)"></div>
  <div class="a" style="left:14px;top:14px;color:#fff;font-size:9px;font-weight:300">Our Mockup Area</div>
  <div class="a" style="left:14px;top:43px;width:125px"><div class="hd w" style="font-size:6px">Heading Here</div><div class="tiny w">Lorem ipsum dolor sit amet consectetur adipiscing elit, sed do eiusmod tempor incididunt ut labore et dolore magna aliqua. Ut enim minim veniam, quis nostrud exercitation.</div></div>
  <div class="a" style="left:14px;top:105px;width:130px;display:flex;flex-direction:column;gap:9px">
    <div style="display:flex;gap:6px"><span class="ic r" style="flex:none"></span><span class="tiny">Lorem ipsum dolor sit amet, consectetur adipiscing elit, sed do eiusmod tempor incididunt ut labore et dolore magna aliqua.</span></div>
    <div style="display:flex;gap:6px"><span class="ic" style="flex:none;background:var(--slate)"></span><span class="tiny">Lorem ipsum dolor sit amet, consectetur adipiscing elit, sed do eiusmod tempor incididunt ut labore et dolore magna aliqua.</span></div>
  </div>
  <svg class="a" style="left:145px;top:0" width="193" height="190" viewBox="0 0 193 190">
    <rect x="3" y="14" width="185" height="128" rx="4" fill="#15161a"/>
    <rect x="9" y="20" width="173" height="110" fill="#fff"/>
    <rect x="3" y="130" width="185" height="12" fill="#d6d8dc"/>
    <path d="M82 142 H110 L114 160 H78 Z" fill="#b9bcc2"/>
  </svg>
  <div class="brand" style="left:154px;width:173px;top:68px;justify-content:center;font-size:19px"><i style="width:6px;height:6px"></i>RivoPlex</div>
  <div class="mark"></div>
  <div class="foot">© Copyright 2017 RivoPlex. All rights reserved.</div><div class="pg">7</div>
</section>

<!-- 17 line chart -->
<section class="slide">
  <div class="a" style="left:23px;top:36px;font-size:12px;font-weight:300;color:var(--ink);line-height:15px">This Is Line<br>Chart Slide</div>
  <div class="a" style="left:23px;top:75px;width:76px;height:11px;background:var(--red);color:#fff;font-size:5px;text-align:center;line-height:11px">Creative Text Here</div>
  <div class="a tiny" style="left:28px;top:108px;width:82px"><b style="color:var(--ink)">Lorem ipsum dolor</b> sit amet, consectetur adipiscing elit, sed do eiusmod tempor incididunt ut labore et commodo consequat dolore magna aliqua.</div>
  <svg class="a" style="left:136px;top:36px" width="196" height="142" viewBox="0 0 196 142">
    <g fill="#999" font-size="3" font-family="Open Sans,sans-serif" text-anchor="end"><text x="8" y="4">5</text><text x="8" y="17">4.5</text><text x="8" y="30">4</text><text x="8" y="43">3.5</text><text x="8" y="56">3</text><text x="8" y="69">2.5</text><text x="8" y="82">2</text><text x="8" y="95">1.5</text><text x="8" y="108">1</text><text x="8" y="121">0.5</text><text x="8" y="134">0</text></g>
    <g fill="#999" font-size="3" font-family="Open Sans,sans-serif" text-anchor="middle"><text x="30" y="140">Category 1</text><text x="75" y="140">Category 2</text><text x="118" y="140">Category 3</text><text x="162" y="140">Category 4</text></g>
    <polyline points="30,30 75,82 118,60 162,12" fill="none" stroke="var(--dark)" stroke-width="1.2"/>
    <polyline points="30,82 75,20 118,74 162,56" fill="none" stroke="var(--red)" stroke-width="1.2"/>
  </svg>
</section>

<!-- 18 image grid -->
<section class="slide">
  <div class="title">Your Title Goes Here</div>
  <div class="brand sm"><i></i>RivoPlex</div>
  <div class="a" style="left:24px;top:48px;width:290px;height:117px;display:grid;grid-template-columns:repeat(3,1fr);grid-template-rows:1fr 1fr;gap:2px">
    <div class="photo steel" style="position:relative" role="img" aria-label="City street between tall buildings"></div>
    <div style="background:var(--slate);padding:7px 5px"><div class="hd w" style="font-size:7px">Heading Goes Here</div><div class="tiny w">Lorem ipsum dolor sit amet consectetur adipiscing elit, sed do eiusmod tempor incididunt ut labore.</div></div>
    <div class="photo glass" style="position:relative" role="img" aria-label="Glass office tower"></div>
    <div style="background:var(--red);padding:7px 5px"><div class="hd w" style="font-size:7px">Heading Goes Here</div><div class="tiny w">Lorem ipsum dolor sit amet consectetur adipiscing elit, sed do eiusmod tempor incididunt ut labore.</div></div>
    <div class="photo sky" style="position:relative" role="img" aria-label="Towers converging into the sky"></div>
    <div style="background:var(--dark);padding:7px 5px"><div class="hd w" style="font-size:7px">Heading Goes Here</div><div class="tiny w">Lorem ipsum dolor sit amet consectetur adipiscing elit, sed do eiusmod tempor incididunt ut labore.</div></div>
  </div>
  <div class="mark"></div>
  <div class="foot">© Copyright 2017 RivoPlex. All rights reserved.</div><div class="pg">8</div>
</section>

</main>
</body>
</html>
```